Real Estate Agent Announcement

I need an announcement postcard designed with imagery almost exactly similar to below; one side imagery and copy on the other. Palette is either desired in neutrals: off white, warm white, or very soft grey. I'd like to stick as close to example below in feeling of image evoking opulence and text to be clean and elegant. need double sided card with simple logo on the back. copy of logo attached. editable file type.

Target Market(s)

Luxury real estate market northern california

Industry/Entity Type

Real Estate

Font styles to use
Serif

```html
<!DOCTYPE html>
<html lang="en">
<head>
<meta charset="UTF-8">
<title>Elena Marchetti – Announcement Postcard</title>
<link rel="stylesheet" href="https://fonts.googleapis.com/css2?family=Marcellus&display=swap">
<style>
  :root {
    --page: #ffffff;
    --slate: #5b5b66;
    --ink-light: #f4f3f1;
    --ink-soft: #e3e2e0;
    --photo-light: #f3efe8;
    --photo-mid: #ddd5c8;
    --photo-deep: #a89f92;
  }
  * { box-sizing: border-box; margin: 0; padding: 0; }
  html, body {
    width: 805px;
    height: 1200px;
    overflow: hidden;
    background: var(--page);
  }
  body {
    position: relative;
    font-family: "Marcellus", Georgia, serif;
    color: var(--ink-light);
  }
  .card {
    position: absolute;
    left: 0;
    width: 805px;
    background: var(--slate);
  }
  .card--front { top: 0; height: 577px; }
  .card--back { top: 622px; height: 578px; }

  .front-photo {
    position: absolute;
    left: 0; top: 0;
    width: 370px; height: 577px;
    background:
      linear-gradient(180deg, rgba(255,255,255,0.35) 0%, rgba(255,255,255,0) 45%),
      linear-gradient(90deg, var(--photo-light) 0%, var(--photo-mid) 55%, var(--photo-deep) 100%);
  }
  .front-copy {
    position: absolute;
    left: 370px; top: 0;
    width: 435px; height: 577px;
    text-align: center;
  }
  .agent-name {
    font-weight: 400;
    letter-spacing: 0.5px;
  }
  .front-copy .agent-name {
    position: absolute;
    top: 180px; left: 0; right: 0;
    font-size: 46px;
  }
  .affiliation {
    position: absolute;
    top: 250px; left: 0; right: 0;
    font-size: 11px;
    color: var(--ink-soft);
  }
  .tagline {
    position: absolute;
    top: 300px; left: 0; right: 0;
    font-size: 17px;
    line-height: 28px;
    color: var(--ink-soft);
  }

  .back-copy {
    position: absolute;
    inset: 0;
    text-align: center;
  }
  .back-copy .agent-name {
    position: absolute;
    top: 66px; left: 0; right: 0;
    font-size: 44px;
  }
  .address {
    position: absolute;
    top: 160px; left: 0; right: 0;
    font-size: 21px;
    line-height: 37px;
    font-style: normal;
    color: var(--ink-soft);
  }
  .contact-line {
    position: absolute;
    left: 0; right: 0;
    font-size: 19px;
    color: var(--ink-soft);
  }
  .contact-phone { top: 246px; }
  .contact-email { top: 297px; }
  .contact-web   { top: 345px; }

  .social-row {
    position: absolute;
    top: 438px;
    left: 0; right: 0;
    display: flex;
    justify-content: center;
    gap: 12px;
  }
  .social-dot {
    width: 42px; height: 42px;
    border-radius: 50%;
    background: var(--ink-soft);
  }
</style>
</head>
<body>
  <section class="card card--front">
    <div class="front-photo" role="img" aria-label="Bright, elegant entry hall with a tufted sofa, white walls, tall windows and a polished floor"></div>
    <div class="front-copy">
      <h1 class="agent-name">Elena Marchetti</h1>
      <p class="affiliation">is pleased to announce her affiliation with Harbor &amp; Vale Realty</p>
      <p class="tagline">Bringing you knowledge, integrity, reliability<br>and most importantly, your perfect home.</p>
    </div>
  </section>

  <section class="card card--back">
    <div class="back-copy">
      <h2 class="agent-name">Elena Marchetti</h2>
      <address class="address">1480 Alder Grove Ave. Ste. 300<br>Lafayette, CA&nbsp; 94549</address>
      <p class="contact-line contact-phone">(925) 555-0148</p>
      <p class="contact-line contact-email">elena@elenamarchetti.com</p>
      <p class="contact-line contact-web">www.elenamarchetti.com</p>
      <div class="social-row" aria-label="Social profiles">
        <span class="social-dot"></span>
        <span class="social-dot"></span>
        <span class="social-dot"></span>
        <span class="social-dot"></span>
      </div>
    </div>
  </section>
</body>
</html>
```